Glimmora Pages with Bold Font

I want the font to be simple yet bold for Glimmora images. Its all about a simple bold readable font. I need a single glimmora page with an image and copy/text on or over the image. The words will change in the future. I'm looking for the right font. I like fiery red and yellow colors. The "One Pic" attached is a sample of what I want without the Veltrix words.

```html
<!DOCTYPE html>
<html lang="en">
<head>
<meta charset="UTF-8">
<title>Glimmora Page – Trainer for Men</title>
<link rel="stylesheet" href="https://fonts.googleapis.com/css2?family=Abril+Fatface&family=Anton&family=Poppins:wght@400;600;700&display=swap">
<style>
  :root {
    --sheet-top: #ffab96;
    --sheet-bottom: #ff6478;
    --fiery-red: #dc1717;
    --fiery-red-deep: #c30f12;
    --fiery-orange: #f0441f;
    --headline-yellow: #ffd200;
    --copy-white: #ffffff;
    --photo-light: #e9b08e;
    --photo-mid: #c98861;
    --photo-dark: #9a5a3c;
  }
  * { margin: 0; padding: 0; box-sizing: border-box; }
  html, body { width: 1200px; height: 1200px; overflow: hidden; }
  body {
    position: relative;
    background: linear-gradient(180deg, var(--sheet-top) 0%, var(--sheet-bottom) 100%);
    font-family: "Poppins", sans-serif;
    color: var(--copy-white);
  }
  .sheet-title {
    position: absolute; top: 24px; left: 0; width: 100%;
    text-align: center; font-weight: 700; font-size: 31px; letter-spacing: 0.5px;
  }
  .sheet-subtitle {
    position: absolute; top: 70px; left: 0; width: 100%;
    text-align: center; font-weight: 400; font-size: 19px;
  }
  .post {
    position: absolute; left: 157px; top: 157px; width: 886px; height: 886px;
    overflow: hidden;
    background:
      radial-gradient(ellipse 55% 60% at 48% 50%, var(--fiery-orange) 0%, rgba(240,68,31,0) 70%),
      linear-gradient(160deg, var(--fiery-red) 0%, var(--fiery-red-deep) 100%);
    box-shadow: 6px 10px 14px rgba(90, 20, 20, 0.35);
  }
  .post-photo {
    position: absolute; left: 0; top: 0; width: 400px; height: 886px;
    background: linear-gradient(180deg, var(--photo-light) 0%, var(--photo-mid) 45%, var(--photo-dark) 100%);
    border-radius: 0 180px 40px 0;
  }
  .trainer-name {
    position: absolute; right: 18px; top: 18px;
    font-family: "Abril Fatface", serif; font-size: 37px; line-height: 1;
  }
  .trainer-role {
    position: absolute; right: 18px; top: 62px;
    font-weight: 400; font-size: 28px; line-height: 1;
  }
  .headline {
    position: absolute; right: 20px;
    font-family: "Anton", sans-serif; color: var(--headline-yellow);
    line-height: 1; text-transform: uppercase; white-space: nowrap;
    text-shadow: 2px 2px 2px rgba(80, 0, 0, 0.45);
  }
  .headline-big { font-size: 70px; }
  .headline-mid { font-size: 54px; }
  .headline-help { font-size: 70px; }
  .line-1 { top: 110px; }
  .line-2 { top: 185px; }
  .line-3 { top: 250px; }
  .line-4 { top: 324px; }
  .line-5 { top: 398px; }
  .line-5 .small { font-size: 55px; }
  .body-copy {
    position: absolute; right: 30px; top: 512px;
    text-align: right; font-weight: 700; font-size: 33px; line-height: 49.5px;
    text-shadow: 1px 1px 2px rgba(80, 0, 0, 0.35);
  }
</style>
</head>
<body>
  <h1 class="sheet-title">Glimmora Image: 1080px X 1080px</h1>
  <p class="sheet-subtitle">High Definition PSD file with JPG, PNG, GIF and PDF file &nbsp;|&nbsp; Fonts will be providee with the design source files</p>

  <section class="post">
    <div class="post-photo" role="img" aria-label="Cut-out photograph of a woman model posing, on the left side of the post"></div>

    <p class="trainer-name">Maren Joy Colby</p>
    <p class="trainer-role">TRAINER FOR MEN</p>

    <p class="headline headline-big line-1">Wanna</p>
    <p class="headline headline-mid line-2">Loose weight?</p>
    <p class="headline headline-big line-3">Wanna</p>
    <p class="headline headline-mid line-4">Shrink that gut?</p>
    <p class="headline headline-help line-5"><span class="small">I can</span> Help <span class="small">you.</span></p>

    <p class="body-copy">
      The sectret to find what<br>
      works for you!<br>
      And I can give you that.<br>
      The pounds will melt away,<br>
      your gut will shrink<br>
      and your health will<br>
      improve.
    </p>
  </section>
</body>
</html>
```